QV Holdings Website Redesign Contest

We want to refresh our website to be more insitutional, professional for an international audience. We have designed a new logo for this purpose and that has been attached. A full brand brief and positioning statement has also been attached. Please read through all the documents carefully before designing. The old website is found here: https://qv-holdings.example/

Target Market(s)

Actuaries and associated businesses internationally

Industry/Entity Type

professional services - actuaries

Number of Pages Required

3 page

Font styles to use
Sans Serif

Colors
0054AA
0677BA
7BADD7
CADEEF
E8F1F8
0094D4
00A9DD
6FCCEA
C7EBF8
E9F6FB
F0912C
F2A743
F7CA91
FBE8D2
FDF5EE
EE7325
F08F49
F5BC92
FAE3D3
FDF4ED
EB3D1F
EC4F4E
F09395
F8D3D4
FCEDEE

Requirements
Must have
• blues and greens to match the logo color, complimentary colors, navigation
Nice to have
• old site: https://qv-holdings.example/

```html
<!DOCTYPE html>
<html lang="en">
<head>
<meta charset="utf-8">
<title>QV Holdings — Actuarial Software</title>
<link rel="stylesheet" href="https://fonts.googleapis.com/css2?family=Lexend:wght@300;400;500;600&display=swap">
<style>
:root{
  --navy:#0054AA;
  --blue:#0677BA;
  --sky:#7BADD7;
  --mist:#CADEEF;
  --ice:#E8F1F8;
  --orange:#EE7325;
  --amber:#F0912C;
  --peach:#FDF4ED;
  --peach-2:#FAE3D3;
  --ink:#1d2433;
  --text:#3c4454;
  --muted:#6c7486;
  --panel:#f3f5fa;
  --white:#ffffff;
  --footer:#0a4d9c;
}
*{box-sizing:border-box;margin:0;padding:0}
html,body{width:1200px;height:4008px;overflow:hidden}
body{font-family:"Lexend",sans-serif;color:var(--text);background:var(--white)}
.page{position:relative;width:1200px;height:4008px;overflow:hidden;background:var(--white)}
.abs{position:absolute}
.hl{color:var(--amber)}
.btn{display:inline-flex;align-items:center;justify-content:center;border-radius:24px;font-size:13px;font-weight:400;text-transform:uppercase;letter-spacing:.2px;white-space:nowrap}
.btn-solid{background:var(--orange);color:var(--white)}
.btn-line{border:1.5px solid var(--orange);color:var(--ink);background:var(--white)}
.section-title{position:absolute;left:0;width:1200px;text-align:center;font-size:31px;font-weight:500;letter-spacing:-.5px;text-transform:uppercase;color:var(--navy)}
.section-title span{margin-left:22px}

/* header + hero */
.hero-bg{left:0;top:0;width:1200px;height:480px;background:linear-gradient(#fafbfd,#f4f6fa)}
.brand{font-size:27px;font-weight:500;letter-spacing:2px;color:var(--navy);display:flex;align-items:center;gap:10px}
.brand .dot{width:14px;height:14px;border-radius:50%;background:var(--orange)}
.menu{left:1050px;top:38px;width:36px;height:36px;border-radius:50%;background:var(--peach-2);display:flex;flex-direction:column;justify-content:center;align-items:center;gap:3px}
.menu i{display:block;width:12px;height:2px;background:var(--ink)}
.hero-title{left:0;top:122px;width:1200px;text-align:center;font-size:30px;font-weight:500;line-height:47px;letter-spacing:-.6px;color:var(--navy);text-transform:uppercase}
.hero-sub{left:190px;top:230px;width:820px;text-align:center;font-size:16px;line-height:34px;font-weight:300;color:var(--ink)}

/* solutions */
.solutions-title{color:var(--white);top:508px}
.card{top:607px;width:310px;height:333px;border-radius:16px;background:rgba(255,255,255,.06);text-align:center;color:var(--white);padding-top:42px}
.card .ico{width:84px;height:84px;margin:0 auto 24px;border-radius:50%;border:1.5px dashed var(--amber);display:flex;align-items:center;justify-content:center}
.card .ico span{width:38px;height:38px;border-radius:8px;background:var(--mist)}
.card h3{font-size:21px;font-weight:500;line-height:37px;color:var(--white);text-transform:uppercase;letter-spacing:-.3px}
.card p{font-size:16px;line-height:34px;font-weight:300;margin-top:8px;padding:0 24px}

/* overview */
.overview{left:110px;top:1027px;width:978px;height:913px;border-radius:24px;background:var(--panel)}
.ov-box{left:232px;width:736px;background:var(--white);border:1px solid #e2e6ef;border-radius:12px}
.ov-head{text-align:center;font-size:17px;color:var(--navy);text-transform:uppercase;font-weight:400;padding:14px 0;border-bottom:1px solid #e6e9f0}
.sources{display:flex;justify-content:space-around;padding:22px 40px 0}
.src{display:flex;align-items:center;gap:22px;font-size:15px;line-height:30px;text-transform:uppercase;color:var(--ink)}
.src .si{width:40px;height:42px;border-radius:6px;background:linear-gradient(135deg,var(--mist),var(--peach-2))}
.engine-sub{text-align:center;font-size:15px;font-weight:500;color:var(--ink);text-transform:uppercase;margin:0 44px;padding:4px 0 8px;border-bottom:1px solid #e6e9f0}
.modules{display:flex;gap:20px;padding:38px 28px 0}
.mod{width:155px;height:124px;border-radius:14px;background:var(--peach);text-align:center;font-size:15px;color:var(--ink);text-transform:uppercase;padding-top:24px}
.mod .mi{width:46px;height:46px;margin:0 auto 18px;border-radius:8px;background:linear-gradient(135deg,var(--mist),var(--peach-2))}
.outputs{text-align:center;font-size:15px;font-weight:500;color:var(--ink);text-transform:uppercase;padding-top:18px;letter-spacing:-.2px}
.outputs b{font-weight:400;margin:0 10px;color:var(--muted)}
.ov-text{left:160px;top:1826px;width:880px;text-align:center;font-size:16px;line-height:34px;font-weight:300;color:var(--ink)}

/* characteristics */
.stage{left:626px;width:480px}
.stage h4{font-size:21px;font-weight:500;color:var(--ink);text-transform:uppercase;line-height:30px}
.stage h4 span{color:var(--sky);font-weight:400}
.stage p{font-size:17px;line-height:36px;color:var(--muted);text-transform:uppercase;font-weight:400;margin-top:10px;letter-spacing:-.3px}
.ring{width:126px;height:126px;border-radius:50%;background:var(--white);display:flex;align-items:center;justify-content:center}
.ring span{width:56px;height:56px;border-radius:10px;background:linear-gradient(135deg,var(--mist),var(--peach-2))}
.diag-brand{left:200px;top:2350px;width:240px;text-align:center;font-size:26px;font-weight:500;letter-spacing:2px;color:var(--navy)}

/* insights */
.insight-card{left:110px;top:2879px;width:460px;height:505px;background:var(--white);border-radius:20px;box-shadow:0 6px 30px rgba(20,40,90,.08);padding:42px 36px}
.insight-card h3,.insight h3{font-size:20px;line-height:39px;font-weight:500;color:var(--navy);text-transform:uppercase;letter-spacing:-.4px}
.insight-card p,.insight p{font-size:16px;line-height:34px;font-weight:300;color:var(--ink)}
.insight-card p{margin-top:22px}
.insight-card p + p{margin-top:12px;text-align:justify}
.insight{left:632px;width:456px}
.insight p{margin-top:10px;height:68px;overflow:hidden}

/* cta + footer */
.cta{left:0;top:3568px;width:1200px;height:140px;background:var(--navy);border-radius:48px 48px 0 0}
.cta h2{position:absolute;left:110px;top:48px;font-size:23px;font-weight:500;color:var(--white);text-transform:uppercase;letter-spacing:-.4px}
.footer{left:0;top:3688px;width:1200px;height:320px;background:var(--footer)}
.footer h5{font-size:19px;font-weight:500;color:var(--white);text-transform:uppercase}
.footer h5:after{content:"";display:block;width:36px;height:2px;background:var(--orange);margin-top:12px}
.links a{display:block;font-size:14px;color:var(--white);text-decoration:none;line-height:36px;text-transform:uppercase}
.contact-row{display:flex;align-items:center;gap:16px;font-size:14px;color:var(--white);text-transform:uppercase;height:58px}
.contact-row .ci{width:34px;height:34px;border-radius:50%;background:var(--white);display:flex;align-items:center;justify-content:center;flex:none}
</style>
</head>
<body>
<div class="page">

  <!-- Header & hero -->
  <div class="abs hero-bg"></div>
  <div class="abs brand" style="left:110px;top:36px"><span class="dot"></span>QV HOLDINGS</div>
  <a class="abs btn btn-line" style="left:740px;top:38px;width:282px;height:36px">Request a technical walkthrough</a>
  <div class="abs menu"><i></i><i></i><i></i></div>

  <h1 class="abs hero-title">Actuarial <span class="hl">software for structured</span>, auditable<br>financial analysis</h1>
  <p class="abs hero-sub">Software that translates actuarial methodologies into disciplined decision-ready analytical tools across diverse regulatory environments.</p>
  <a class="abs btn btn-solid" style="left:436px;top:328px;width:328px;height:44px">Request a technical walkthrough</a>

  <!-- Blue solutions band -->
  <svg class="abs" style="left:0;top:442px" width="1200" height="780" viewBox="0 0 1200 780" aria-hidden="true">
    <path d="M0 70 Q0 0 70 0 H1130 Q1200 0 1200 70 V640 C1020 770 480 640 0 760 Z" fill="#0054AA"/>
  </svg>
  <h2 class="section-title solutions-title">Our core <span>solutions</span></h2>

  <div class="abs card" style="left:110px">
    <div class="ico"><span role="img" aria-label="Reserving document icon"></span></div>
    <h3>Reserving &amp; valuation</h3>
    <p>Software supporting structured reserving workflows and financial reporting across jurisdictions</p>
  </div>
  <div class="abs card" style="left:445px">
    <div class="ico"><span role="img" aria-label="Pricing icon"></span></div>
    <h3>Pricing</h3>
    <p>Models supporting insurance and reinsurance pricing based on actuarial methodologies</p>
  </div>
  <div class="abs card" style="left:780px">
    <div class="ico"><span role="img" aria-label="Risk checklist icon"></span></div>
    <h3>Enterprise risk<br>management</h3>
    <p>Software supporting reinsurance optimization and capital modeling</p>
  </div>

  <!-- Platform overview -->
  <div class="abs overview"></div>
  <h2 class="section-title" style="top:1074px">Platform <span>overview</span></h2>

  <div class="abs ov-box" style="top:1164px;height:148px">
    <div class="ov-head">Data sources</div>
    <div class="sources">
      <div class="src"><div class="si" role="img" aria-label="Policy data icon"></div><div>Policy<br>data</div></div>
      <div class="src"><div class="si" role="img" aria-label="Claims data icon"></div><div>Claims<br>data</div></div>
      <div class="src"><div class="si" role="img" aria-label="Market data icon"></div><div>Market<br>data</div></div>
    </div>
  </div>

  <svg class="abs" style="left:586px;top:1314px" width="28" height="36" viewBox="0 0 28 36" aria-hidden="true">
    <rect x="10" y="0" width="8" height="20" fill="#c9ced8"/><path d="M2 18 H26 L14 34 Z" fill="#c9ced8"/>
  </svg>

  <div class="abs ov-box" style="top:1351px;height:267px">
    <div class="ov-head" style="border:0;padding-bottom:8px;padding-top:22px">Actuarial engine</div>
    <div class="engine-sub">Modular platform core</div>
    <div class="modules">
      <div class="mod"><div class="mi" role="img" aria-label="Reserving icon"></div>Reserving</div>
      <div class="mod"><div class="mi" role="img" aria-label="Valuation icon"></div>Valuation</div>
      <div class="mod"><div class="mi" role="img" aria-label="Pricing icon"></div>Pricing</div>
      <div class="mod"><div class="mi" role="img" aria-label="Risk analysis icon"></div>Risk analysis</div>
    </div>
  </div>

  <svg class="abs" style="left:232px;top:1618px" width="736" height="70" viewBox="0 0 736 70" aria-hidden="true">
    <g stroke="#d3d8e2" stroke-width="1.5" fill="none">
      <path d="M95 0 V34 H641 V0"/><path d="M280 0 V34"/><path d="M455 0 V34"/>
    </g>
    <rect x="364" y="36" width="8" height="16" fill="#c9ced8"/><path d="M356 50 H380 L368 66 Z" fill="#c9ced8"/>
  </svg>

  <div class="abs ov-box" style="top:1688px;height:105px">
    <div class="ov-head" style="padding:12px 0">Outputs</div>
    <div class="outputs">Reports<b>·</b>Regulatory filings<b>·</b>Dashboards<b>·</b>Scenario analysis</div>
  </div>

  <p class="abs ov-text">QV Holdings develops modular actuarial software designed to support reserving, valuation, pricing, and risk analysis workflows across diverse regulatory environments.</p>
  <a class="abs btn btn-solid" style="left:501px;top:1920px;width:198px;height:42px">Explore platform</a>

  <!-- Characteristics -->
  <h2 class="section-title" style="top:2040px">Platform <span>characteristics</span></h2>

  <svg class="abs" style="left:100px;top:2140px" width="460" height="450" viewBox="0 0 460 450" aria-hidden="true">
    <path d="M152 62 Q230 35 300 68" stroke="#EE7325" stroke-width="6" fill="none" stroke-linecap="round"/>
    <path d="M290 52 L310 74 L282 80 Z" fill="#EE7325"/>
    <path d="M368 152 Q390 225 370 282" stroke="#0054AA" stroke-width="5" fill="none" stroke-linecap="round"/>
    <path d="M356 276 L370 302 L384 278 Z" fill="#0054AA"/>
    <path d="M300 352 Q230 388 160 362" stroke="#EE7325" stroke-width="6" fill="none" stroke-linecap="round"/>
    <path d="M170 348 L144 360 L166 378 Z" fill="#EE7325"/>
    <path d="M74 290 Q52 220 74 164" stroke="#0054AA" stroke-width="5" fill="none" stroke-linecap="round"/>
    <path d="M62 170 L76 144 L90 170 Z" fill="#0054AA"/>
  </svg>
  <div class="abs ring" style="left:113px;top:2154px;border:3px solid #6FCCEA"><span role="img" aria-label="Workflow settings icon"></span></div>
  <div class="abs ring" style="left:410px;top:2154px;border:3px solid #0054AA"><span role="img" aria-label="Review icon"></span></div>
  <div class="abs ring" style="left:113px;top:2444px;border:3px solid #0677BA"><span role="img" aria-label="Scenario chart icon"></span></div>
  <div class="abs ring" style="left:410px;top:2444px;border:3px solid #7BADD7"><span role="img" aria-label="Judgment checklist icon"></span></div>
  <div class="abs diag-brand">QV HOLDINGS</div>

  <div class="abs stage" style="top:2116px"><h4>Stage <span>01</span></h4><p>Structured workflows suitable for multi jurisdictional review</p></div>
  <div class="abs stage" style="top:2257px"><h4>Stage <span>02</span></h4><p>Transparent assumptions and methodological clarity</p></div>
  <div class="abs stage" style="top:2398px"><h4>Stage <span>03</span></h4><p>Comparative scenario analysis</p></div>
  <div class="abs stage" style="top:2502px"><h4>Stage <span>04</span></h4><p>Supports professional judgment rather than replacing it</p></div>

  <!-- Insights -->
  <svg class="abs" style="left:0;top:2680px" width="1200" height="888" viewBox="0 0 1200 888" aria-hidden="true">
    <path d="M0 110 C300 0 800 120 1200 20 V888 H0 Z" fill="#f5f7fb"/>
  </svg>
  <h2 class="section-title" style="top:2785px">Latest <span>insights &amp; news</span></h2>

  <article class="abs insight-card">
    <h3>Methodological perspectives in actuarial reserving</h3>
    <p>Exploring evolving approaches to actuarial reserving, including methodological transparency, model assumptions, and the balance between analytical rigor and professional judgment.</p>
    <p>QV Holdings shares research, observations, and professional perspectives on actuarial methods, regulatory developments.</p>
    <a class="btn btn-solid" style="width:148px;height:42px;margin-top:28px">Read insights</a>
  </article>

  <article class="abs insight" style="top:2868px">
    <h3>Governance considerations in multi jurisdictional analysis</h3>
    <p>Examining how actuarial teams structure governance processes when models and assumptions must satisfy multiple</p>
    <a class="btn btn-line" style="width:148px;height:42px;margin-top:18px">Read insights</a>
  </article>
  <div class="abs" style="left:632px;top:3132px;width:456px;height:1px;background:#d9dde6"></div>
  <article class="abs insight" style="top:3160px">
    <h3>Observations on actuarial practice in emerging markets</h3>
    <p>Insights into the unique analytical challenges and opportunities present in emerging insurance markets including</p>
    <a class="btn btn-line" style="width:148px;height:42px;margin-top:18px">Read insights</a>
  </article>

  <a class="abs btn btn-solid" style="left:504px;top:3440px;width:192px;height:42px">View more insights</a>

  <!-- CTA -->
  <div class="abs cta">
    <h2>Interested in exploring the platform?</h2>
    <a class="btn btn-solid" style="position:absolute;left:772px;top:40px;width:316px;height:42px">Request a technical walkthrough</a>
  </div>

  <!-- Footer -->
  <footer class="abs footer">
    <div class="abs brand" style="left:110px;top:60px;color:#fff;font-size:32px"><span class="dot"></span>QV HOLDINGS</div>
    <p class="abs" style="left:110px;top:140px;font-size:13px;color:#fff">COPYRIGHT @2026 . ALL RIGHTS RESERVED</p>
    <div class="abs" style="left:110px;top:184px;width:34px;height:34px;border-radius:50%;background:#fff" role="img" aria-label="Social profile link"></div>

    <div class="abs" style="left:583px;top:56px">
      <h5>Quick links</h5>
      <nav class="links" style="margin-top:18px">
        <a>Company</a><a>Platform</a><a>Solutions</a><a>Insights</a><a>Contact</a>
      </nav>
    </div>

    <div class="abs" style="left:856px;top:56px">
      <h5>Contact</h5>
      <div style="margin-top:24px">
        <div class="contact-row"><span class="ci"><svg width="16" height="16" viewBox="0 0 24 24"><path d="M6.6 10.8a15 15 0 006.6 6.6l2.2-2.2a1 1 0 011-.25 11.4 11.4 0 003.6.6 1 1 0 011 1V20a1 1 0 01-1 1A17 17 0 013 4a1 1 0 011-1h3.5a1 1 0 011 1c0 1.25.2 2.45.6 3.6a1 1 0 01-.25 1z" fill="#0054AA"/></svg></span>+1 (555) 010-2048</div>
        <div class="contact-row"><span class="ci"><svg width="16" height="16" viewBox="0 0 24 24"><rect x="3" y="5" width="18" height="14" rx="2" fill="#0054AA"/><path d="M3 7l9 6 9-6" stroke="#fff" stroke-width="1.6" fill="none"/></svg></span>HELLO@QV-HOLDINGS.EXAMPLE</div>
        <div class="contact-row"><span class="ci"><svg width="16" height="16" viewBox="0 0 24 24"><circle cx="12" cy="12" r="9" stroke="#0054AA" stroke-width="2" fill="none"/><path d="M3 12h18M12 3c3 3 3 15 0 18M12 3c-3 3-3 15 0 18" stroke="#0054AA" stroke-width="1.6" fill="none"/></svg></span>WWW.QV-HOLDINGS.EXAMPLE</div>
      </div>
    </div>
  </footer>

</div>
</body>
</html>
```